My garage customisation company needs a business card

I need a business card design for my company "Shed Wizards"
I provide fully customised garage solutions for your previously cluttered, waste of space. My logo was just completed and can be provided if needed. I need the card to be clean, classy and eye catching.
Thank you

Target Market(s)

Men and Woman Home Owners

Industry/Entity Type

Business

Contact Information for Business Card

Jonathan Pell
jon@shedwizards.net
shedwizards.net

It's Time To Take Back Your Garage... From simple storage solutions to fully customised from the floor up, we've got you covered.

Requirements
Must have
• Logo
• Name
• Email Address
• Website
• Brief Description of what we do
Nice to have
• Back ground picture of Before and After

```html
<!DOCTYPE html>
<html lang="en">
<head>
<meta charset="utf-8">
<title>Shed Wizards – Business Card</title>
<link rel="stylesheet" href="https://fonts.googleapis.com/css2?family=Nunito:wght@400;700;800&family=Josefin+Sans:wght@600&display=swap">
<style>
  :root {
    --page: #ffffff;
    --card-dark: #1c1c1c;
    --card-dark-edge: #0d0d0d;
    --orange: #ee8a1f;
    --orange-deep: #d85a1a;
    --orange-band-top: #ec7d1a;
    --text-light: #f2f2f2;
    --text-ink: #111111;
  }
  * { box-sizing: border-box; margin: 0; padding: 0; }
  html, body {
    width: 1200px; height: 1200px; overflow: hidden;
    background: var(--page);
    font-family: "Nunito", sans-serif;
  }
  .card {
    position: absolute;
    left: 181px; width: 840px; height: 479px;
    background: radial-gradient(ellipse at 50% 30%, #2b2b2b 0%, var(--card-dark) 55%, var(--card-dark-edge) 100%);
    overflow: hidden;
  }
  .card--front { top: 79px; }
  .card--back  { top: 643px; }

  .brand {
    position: absolute; left: 0; right: 0;
    display: flex; align-items: center; justify-content: center; gap: 18px;
    color: var(--orange);
    font-weight: 800;
  }
  .brand__mark {
    display: inline-block;
    background: var(--orange);
  }
  .card--front .brand { top: 170px; font-size: 78px; }
  .card--front .brand__mark { width: 46px; height: 46px; }
  .card--back .brand { top: 92px; font-size: 54px; }
  .card--back .brand__mark { width: 32px; height: 32px; }

  .website {
    position: absolute; left: 0; right: 0; top: 413px;
    text-align: center;
    color: var(--orange);
    font-weight: 800; font-size: 28px; letter-spacing: 1px;
  }

  .tagline {
    position: absolute; left: 0; right: 0; top: 246px;
    text-align: center;
    color: var(--text-light);
    font-size: 25px; line-height: 30px; letter-spacing: 0.8px; font-weight: 400;
  }
  .tagline strong { font-weight: 700; }

  .contact-band {
    position: absolute; left: 0; right: 0; top: 334px; bottom: 0;
    background: linear-gradient(180deg, var(--orange-band-top) 0%, var(--orange-deep) 100%);
    text-align: center; color: var(--text-ink);
  }
  .contact-band__name {
    margin-top: 32px;
    font-family: "Josefin Sans", sans-serif;
    font-weight: 600; font-size: 38px; letter-spacing: 4px;
    font-variant: small-caps;
  }
  .contact-band__email {
    margin-top: 6px;
    font-size: 24px; letter-spacing: 0.8px;
  }
</style>
</head>
<body>
  <section class="card card--front">
    <div class="brand"><span class="brand__mark"></span>Shed Wizards</div>
    <div class="website">www.shedwizards.net</div>
  </section>

  <section class="card card--back">
    <div class="brand"><span class="brand__mark"></span>Shed Wizards</div>
    <p class="tagline">Offering simple storage solutions to fully customised<br>garages from the ground up, <strong>we've got you covered.</strong></p>
    <div class="contact-band">
      <div class="contact-band__name">Jonathan Pell</div>
      <div class="contact-band__email">jon@shedwizards.net</div>
    </div>
  </section>
</body>
</html>
```